Business Cards

I'd like help creating business cards with the full logo "Veltrona Capital Partners" on the back of the card (navy background with white writing), and abbreviated logo "VCP" on the front. Would like to list name, title, phone number, email, and website listed on front of card. Would like to keep very simple. Front font Arial or similar.

```html
<!DOCTYPE html>
<html lang="en">
<head>
<meta charset="utf-8">
<title>Veltrona Capital Partners — Business Cards</title>
<link rel="stylesheet" href="https://fonts.googleapis.com/css2?family=Arimo:wght@400;700&display=swap">
<style>
  :root {
    --navy: #1c3e6e;
    --sky: #5b8ed6;
    --ink: #111111;
    --paper: #ffffff;
    --rule: #9aa3ad;
    --backdrop: #9a9a9a;
  }
  * { box-sizing: border-box; margin: 0; padding: 0; }
  html, body { width: 1200px; height: 1200px; overflow: hidden; }
  body {
    background: var(--backdrop);
    font-family: "Arimo", Arial, sans-serif;
    position: relative;
  }
  .card {
    position: absolute;
    left: 226px;
    width: 746px;
    height: 435px;
    border-radius: 20px;
    overflow: hidden;
  }
  /* Back side: full company name */
  .card-back {
    top: 122px;
    background: var(--navy);
    color: var(--paper);
    display: flex;
    flex-direction: column;
    align-items: center;
    justify-content: center;
    text-align: center;
    font-weight: 700;
  }
  .wordmark-name {
    font-size: 72px;
    letter-spacing: 2px;
    line-height: 1;
  }
  .wordmark-tag {
    margin-top: 18px;
    font-size: 24px;
    letter-spacing: 7px;
    line-height: 1;
  }
  /* Front side: initials and contact details */
  .card-front {
    top: 669px;
    background: var(--paper);
  }
  .initials {
    position: absolute;
    top: 48px;
    left: 0;
    width: 100%;
    text-align: center;
    color: var(--navy);
    font-weight: 700;
    font-size: 80px;
    line-height: 1;
    letter-spacing: 2px;
  }
  .person {
    position: absolute;
    top: 232px;
    right: calc(746px - 329px);
    text-align: right;
  }
  .person-name {
    color: var(--navy);
    font-weight: 700;
    font-size: 25px;
    line-height: 30px;
  }
  .person-title {
    color: var(--sky);
    font-size: 20px;
    line-height: 28px;
    letter-spacing: 0.5px;
  }
  .divider {
    position: absolute;
    left: 354px;
    top: 212px;
    width: 1px;
    height: 97px;
    background: var(--rule);
  }
  .contact {
    position: absolute;
    left: 380px;
    top: 217px;
    list-style: none;
  }
  .contact li {
    display: flex;
    align-items: center;
    height: 30.5px;
    color: var(--ink);
    font-size: 23px;
  }
  .contact svg {
    width: 16px;
    height: 16px;
    margin-right: 14px;
    fill: var(--sky);
    flex: none;
  }
  .stripe-light {
    position: absolute;
    left: 0; width: 100%;
    top: 397px; height: 5px;
    background: var(--sky);
  }
  .stripe-navy {
    position: absolute;
    left: 0; width: 100%;
    top: 408px; bottom: 0;
    background: var(--navy);
  }
</style>
</head>
<body>
  <section class="card card-back" aria-label="Card back">
    <div class="wordmark-name">VELTRONA</div>
    <div class="wordmark-tag">CAPITAL PARTNERS</div>
  </section>

  <section class="card card-front" aria-label="Card front">
    <div class="initials">VCP</div>

    <div class="person">
      <div class="person-name">Name Surname</div>
      <div class="person-title">TITLE</div>
    </div>

    <div class="divider"></div>

    <ul class="contact">
      <li>
        <svg viewBox="0 0 24 24" aria-hidden="true"><path d="M6.6 10.8a15.1 15.1 0 0 0 6.6 6.6l2.2-2.2c.3-.3.7-.4 1-.2 1.1.4 2.3.6 3.6.6.6 0 1 .4 1 1V20c0 .6-.4 1-1 1A17 17 0 0 1 3 4c0-.6.4-1 1-1h3.5c.6 0 1 .4 1 1 0 1.3.2 2.5.6 3.6.1.3 0 .7-.2 1z"/></svg>
        (555) 214-0389
      </li>
      <li>
        <svg viewBox="0 0 24 24" aria-hidden="true"><path d="M2 5h20v14H2z M3.5 6.5 12 13l8.5-6.5v-.2h-17z" fill-rule="evenodd"/><path d="M2 5h20L12 12.5z" fill="#ffffff" opacity=".6"/></svg>
        name@veltronacp.com
      </li>
      <li>
        <svg viewBox="0 0 24 24" aria-hidden="true"><path d="M12 2a10 10 0 1 0 0 20 10 10 0 0 0 0-20zm-1 2.1V8H7.4c.8-2 2.1-3.5 3.6-3.9zm2 0c1.5.4 2.8 1.9 3.6 3.9H13zM5.1 8h.2c-.2.6-.3 1.3-.4 2H4.1c.2-.7.5-1.4 1-2zm1.7 2c.1-.7.2-1.4.4-2H11v2zm6.2 0V8h3.8c.2.6.3 1.3.4 2zm5.9-2h.1c.5.6.8 1.3 1 2h-.8c-.1-.7-.2-1.4-.3-2zM4.1 12h.8c.1.7.2 1.4.4 2h-.2c-.5-.6-.8-1.3-1-2zm2.7 0H11v2H7.2c-.2-.6-.3-1.3-.4-2zm6.2 0h4.2c-.1.7-.2 1.4-.4 2H13zm6.1 0h.8c-.2.7-.5 1.4-1 2h-.1c.1-.6.2-1.3.3-2zM7.4 16H11v3.9c-1.5-.4-2.8-1.9-3.6-3.9zm5.6 0h3.6c-.8 2-2.1 3.5-3.6 3.9z"/></svg>
        veltronacp.com
      </li>
    </ul>

    <div class="stripe-light"></div>
    <div class="stripe-navy"></div>
  </section>
</body>
</html>
```